Medical Simulation - Creative Graphic for Data

My company needs a creative graph that depicts the rationales (or reasons) our learners chose certain drug options. Basically, our clients not only want to know how many times certain drugs were selected, but the "whys" behind their choices. I would like a PPT graphic that I can use for other deliverables, where I can simply switch out the drug (treatment) names, the "whys" (what we call rationales), and the specific metrics (percentages, "n" numbers, etc), and the graphic will update and adjust to the new information. The title of the graph (or the slide where the graph will live) should be something like "Treatment Rationales" or something to that effect. Include a placeholder for text to go if anyone wants to add an analysis of the graphic later. This placeholder should accommodate 2-3 bullet points of text. We want this graphic to not just be an image, but organized in a way that you would see in a presentation slide, with a title, place holder for analysis (as indicated above), branding colors, and helpful information to understand the graphic (what is included in this post and it's associated attachments).

I've included specific drug names, rationales, and metrics to use for this (please see excel document). If you are going to design the graph directly in PPT, please use the PPT template design included. Please don't feel like you have to use 1 slide only or can have multiple graphs, if that makes sense for you design idea. They just need to fit within the coloring of the PPT. For font, please use Arial. Below is a Google Drive Link to branding colors and vector art.

https://files.brivoshare.net/open?id=4KQ2TrLm8-XpVd71sNcYhWuPzAe

We are open to many variations and design ideas. Please don't feel like you have to limit yourself! I've attached a few ideas that we've had and it may be a good place to start. We would ESPECIALLY like to see a version utilizing the radial graph (similar to the one included in the Rationales_DesignIdeas document).

Please reach out if you have any questions. Thanks!

Industry/Entity Type

Drug

Requirements
Nice to have
• It would be great to see the radial graph as a design variation (see link below)
• http://6.plotvenna.com/products/plotvenna/docs/users-guide/img/Samples/radar-chart-fixed-radius.png

```html
<!DOCTYPE html>
<html lang="en">
<head>
<meta charset="utf-8">
<title>Treatment Rationales</title>
<link rel="stylesheet" href="https://fonts.googleapis.com/css2?family=Arimo:wght@400;700&display=swap">
<style>
  :root {
    --navy: #0b3a5a;
    --blue: #1a6499;
    --sky: #8ccbec;
    --orange: #f79646;
    --grey: #a5a5a5;
    --charcoal: #5a5a5a;
    --text-grey: #7f7f7f;
    --label-grey: #595959;
    --grid: #d9d9d9;
    --white: #ffffff;
  }
  * { box-sizing: border-box; margin: 0; padding: 0; }
  html, body {
    width: 1200px; height: 2250px; overflow: hidden;
    background: var(--white);
    font-family: "Arimo", Arial, sans-serif;
  }
  .page { position: relative; width: 1200px; height: 2250px; }
  .slide {
    position: absolute; left: 12px; width: 1176px; height: 882px;
    background: var(--white);
    box-shadow: 0 8px 16px rgba(0,0,0,.22);
    overflow: hidden;
  }
  .slide--sunburst { top: 120px; }
  .slide--radar { top: 1245px; }
  .top-bar { position: absolute; left: 0; top: 0; width: 100%; height: 25px; background: var(--navy); }
  .section-tag {
    position: absolute; right: 0; top: 30px; width: 258px; height: 27px;
    background: linear-gradient(90deg, rgba(247,150,70,0) 0%, rgba(247,150,70,.55) 45%, var(--orange) 100%);
    color: var(--white); font-weight: 700; font-size: 16px; letter-spacing: 5px;
    text-align: right; padding-right: 16px; line-height: 27px;
  }
  .title-band {
    position: absolute; left: 0; top: 25px; width: 100%; height: 155px;
  }
  .title-band::after {
    content: ""; position: absolute; left: 0; bottom: 0; width: 860px; height: 6px;
    background: linear-gradient(90deg, rgba(0,0,0,.14), rgba(0,0,0,.08) 60%, rgba(0,0,0,0));
    filter: blur(3px);
  }
  .slide-title {
    position: absolute; left: 0; width: 100%; top: 65px;
    text-align: center; color: var(--navy);
    font-size: 60px; font-weight: 700; letter-spacing: .5px; line-height: 60px;
  }
  .chart { position: absolute; left: 0; top: 0; width: 1176px; height: 882px; }
  .analysis {
    position: absolute; left: 781px; top: 610px; width: 335px;
    color: var(--text-grey); font-size: 14px; line-height: 19.5px;
  }
  .analysis h2 { color: var(--navy); font-size: 18px; font-weight: 700; margin-bottom: 6px; }
  .analysis ul { list-style: none; }
  .analysis li { position: relative; padding-left: 20px; }
  .analysis li::before { content: "•"; position: absolute; left: 2px; }
  .footnote {
    position: absolute; left: 40px; top: 802px;
    color: var(--navy); font-size: 13px;
  }
  .bottom-bar {
    position: absolute; left: 0; bottom: 0; width: 100%; height: 26px;
    background: var(--navy); color: var(--white);
    font-size: 12px; text-align: center; line-height: 26px;
  }
  .callout-text { font-size: 17px; }
  .ring-label { fill: var(--white); font-size: 16px; }
  .pct-label { fill: var(--white); font-size: 17px; }
  .axis-label { fill: var(--text-grey); font-size: 22px; font-weight: 700; }
  .tick-label { fill: var(--label-grey); font-size: 16px; }
  .legend-text { fill: var(--label-grey); font-size: 13.5px; }
  .brand-name { fill: var(--navy); font-size: 17px; font-weight: 700; }
</style>
</head>
<body>
<main class="page">

  <section class="slide slide--sunburst">
    <div class="top-bar"></div>
    <div class="title-band"><h1 class="slide-title">TREATMENT RATIONALES</h1></div>
    <div class="section-tag">EDUCATION</div>

    <svg class="chart" viewBox="0 0 1176 882" aria-label="Sunburst chart of treatments and rationales">
      <g transform="translate(588 495)">
        <g transform="rotate(-90)" fill="none">
          <circle r="86.5" stroke-width="83" pathLength="360" stroke="var(--navy)" stroke-dasharray="93 360" stroke-dashoffset="0"/>
          <circle r="86.5" stroke-width="83" pathLength="360" stroke="var(--grey)" stroke-dasharray="92 360" stroke-dashoffset="-93"/>
          <circle r="86.5" stroke-width="83" pathLength="360" stroke="var(--orange)" stroke-dasharray="76 360" stroke-dashoffset="-185"/>
          <circle r="86.5" stroke-width="83" pathLength="360" stroke="var(--sky)" stroke-dasharray="50 360" stroke-dashoffset="-261"/>
          <circle r="86.5" stroke-width="83" pathLength="360" stroke="var(--blue)" stroke-dasharray="35 360" stroke-dashoffset="-311"/>
          <circle r="86.5" stroke-width="83" pathLength="360" stroke="var(--charcoal)" stroke-dasharray="14 360" stroke-dashoffset="-346"/>

          <circle r="190" stroke-width="124" pathLength="360" stroke="var(--navy)" stroke-dasharray="93 360" stroke-dashoffset="0"/>
          <circle r="158" stroke-width="60" pathLength="360" stroke="var(--grey)" stroke-dasharray="92 360" stroke-dashoffset="-93"/>
          <circle r="190" stroke-width="124" pathLength="360" stroke="var(--orange)" stroke-dasharray="76 360" stroke-dashoffset="-185"/>
          <circle r="190" stroke-width="124" pathLength="360" stroke="var(--sky)" stroke-dasharray="50 360" stroke-dashoffset="-261"/>
          <circle r="190" stroke-width="124" pathLength="360" stroke="var(--blue)" stroke-dasharray="35 360" stroke-dashoffset="-311"/>
          <circle r="190" stroke-width="124" pathLength="360" stroke="var(--charcoal)" stroke-dasharray="14 360" stroke-dashoffset="-346"/>
        </g>
        <circle r="128" fill="none" stroke="var(--white)" stroke-width="3"/>
        <g stroke="var(--white)" stroke-width="3">
          <line x1="0" y1="-45" x2="0" y2="-252"/>
          <line x1="44.9" y1="2.4" x2="251.6" y2="13.2"/>
          <line x1="-3.9" y1="44.8" x2="-22" y2="251"/>
          <line x1="-44.4" y1="7" x2="-248.9" y2="39.4"/>
          <line x1="-34" y1="-29.5" x2="-190.2" y2="-165.3"/>
          <line x1="-10.9" y1="-43.7" x2="-61" y2="-244.5"/>
          <line x1="-126" y1="-22.2" x2="-248.2" y2="-43.8"/>
        </g>
        <circle r="45" fill="var(--white)"/>
        <text class="brand-name" x="0" y="6" text-anchor="middle">Clinova</text>

        <text class="ring-label" text-anchor="middle" transform="translate(62 -60) rotate(-45)">n = 30</text>
        <text class="ring-label" text-anchor="middle" transform="translate(56 65) rotate(50)">n = 20</text>
        <text class="ring-label" text-anchor="middle" transform="translate(-59 63) rotate(-45)">n = 100</text>
        <text class="ring-label" text-anchor="middle" transform="translate(-83 -20) rotate(15)">n = 50</text>
        <text class="ring-label" text-anchor="middle" transform="translate(-44 -73) rotate(-62)">n = 70</text>

        <text class="pct-label" text-anchor="middle" transform="translate(157 -150) rotate(45)">50%</text>
        <text class="pct-label" text-anchor="middle" transform="translate(-23 -189) rotate(90)" dy="6">8%</text>
        <text class="pct-label" text-anchor="middle" transform="translate(-99 -162) rotate(58)" dy="6">50%</text>
        <text class="pct-label" text-anchor="middle" transform="translate(-171 -82) rotate(22)" dy="6">19%</text>
        <text class="pct-label" text-anchor="middle" transform="translate(-192 0)" dy="6">19%</text>
        <text class="pct-label" text-anchor="middle" transform="translate(-135 168) rotate(45)">18%</text>
      </g>

      <g fill="none" stroke="var(--text-grey)" stroke-width="1.5">
        <polyline points="576,244 595,210 643,210"/>
        <polyline points="726,324 768,282 985,282"/>
        <polyline points="783,385 850,433 870,433"/>
        <polyline points="435,303 411,265 390,265"/>
        <polyline points="357,429 343,457 178,457"/>
        <polyline points="432,562 330,650 210,650"/>
        <polyline points="597,657 621,750 639,750"/>
      </g>
      <g fill="var(--text-grey)">
        <circle cx="576" cy="244" r="4"/>
        <circle cx="726" cy="324" r="4"/>
        <circle cx="783" cy="385" r="4"/>
        <circle cx="435" cy="303" r="4"/>
        <circle cx="357" cy="429" r="4"/>
        <circle cx="432" cy="562" r="4"/>
        <circle cx="597" cy="657" r="4"/>
      </g>

      <text class="callout-text" fill="#4a4a4a" x="646" y="222">oxaliplatin/capecitabine</text>
      <text class="callout-text" fill="#4a4a4a" x="646" y="244">plus bevacizumab</text>
      <text class="callout-text" fill="var(--navy)" x="783" y="305">oxaliplatin/leucovorin/5-FU</text>
      <text class="callout-text" fill="var(--navy)" x="873" y="412">irinotecan/leucovorin/5-FU</text>
      <text class="callout-text" fill="var(--navy)" x="873" y="434">plus cetuximab</text>
      <text class="callout-text" fill="var(--blue)" x="390" y="289" text-anchor="end">oxaliplatin/</text>
      <text class="callout-text" fill="var(--blue)" x="390" y="311" text-anchor="end">capecitabine</text>
      <text class="callout-text" fill="var(--sky)" x="318" y="424" text-anchor="end">oxaliplatin/leucovorin/5-FU</text>
      <text class="callout-text" fill="var(--sky)" x="318" y="446" text-anchor="end">plus bevacizumab</text>
      <text class="callout-text" fill="var(--orange)" x="325" y="620" text-anchor="end">irinotecan/leucovorin/5-FU plus</text>
      <text class="callout-text" fill="var(--orange)" x="325" y="642" text-anchor="end">bevacizumab</text>
      <text class="callout-text" fill="var(--text-grey)" x="645" y="756">irinotecan</text>
    </svg>

    <div class="analysis">
      <h2>Heading Here</h2>
      <p>Sed do eiusmod tempor incididunt ut labore et dolore magna aliqua. Ut enimad minim</p>
      <ul>
        <li>Duis aute irure dolor in reprehenderit in voluptate velit esse cillum</li>
        <li>dolore eu fugiat nulla pariatur. Excepteur sint occaecat cupidatat non</li>
        <li>proident, sunt inculpa qui officia deserunt mollit anim id est laborum.</li>
      </ul>
    </div>
    <p class="footnote">*Learners can select 1-2 rationales for each treatment ordered</p>
    <div class="bottom-bar">Clinova Education Confidential and Proprietary Information</div>
  </section>

  <section class="slide slide--radar">
    <div class="top-bar"></div>
    <div class="title-band"><h1 class="slide-title">TREATMENT RATIONALES</h1></div>
    <div class="section-tag">EDUCATION</div>

    <svg class="chart" viewBox="0 0 1176 882" aria-label="Radar chart of rationales per treatment">
      <g class="legend">
        <line x1="284" y1="226" x2="308" y2="226" stroke="var(--grey)" stroke-width="3"/><circle cx="296" cy="226" r="5" fill="var(--grey)"/>
        <text class="legend-text" x="318" y="231">Treatment</text>
        <line x1="284" y1="252" x2="308" y2="252" stroke="var(--charcoal)" stroke-width="3"/><circle cx="296" cy="252" r="5" fill="var(--charcoal)"/>
        <text class="legend-text" x="318" y="257">Impact on quality of life</text>
        <line x1="284" y1="277" x2="308" y2="277" stroke="var(--orange)" stroke-width="3"/><circle cx="296" cy="277" r="5" fill="var(--orange)"/>
        <text class="legend-text" x="318" y="282">Recent guidelines</text>
        <line x1="648" y1="226" x2="672" y2="226" stroke="var(--navy)" stroke-width="3"/><circle cx="660" cy="226" r="5" fill="var(--navy)"/>
        <text class="legend-text" x="682" y="231">Fewer overall side effects</text>
        <line x1="648" y1="252" x2="672" y2="252" stroke="var(--sky)" stroke-width="3"/><circle cx="660" cy="252" r="5" fill="var(--sky)"/>
        <text class="legend-text" x="682" y="257">Preserves future treatment options</text>
      </g>

      <g transform="translate(588 484.5)">
        <g fill="none" stroke="var(--grid)" stroke-width="1">
          <polygon vector-effect="non-scaling-stroke" transform="scale(34.5)" points="0,-1 .7818,-.6235 .9749,.2225 .4339,.901 -.4339,.901 -.9749,.2225 -.7818,-.6235"/>
          <polygon vector-effect="non-scaling-stroke" transform="scale(69)" points="0,-1 .7818,-.6235 .9749,.2225 .4339,.901 -.4339,.901 -.9749,.2225 -.7818,-.6235"/>
          <polygon vector-effect="non-scaling-stroke" transform="scale(103.5)" points="0,-1 .7818,-.6235 .9749,.2225 .4339,.901 -.4339,.901 -.9749,.2225 -.7818,-.6235"/>
          <polygon vector-effect="non-scaling-stroke" transform="scale(138)" points="0,-1 .7818,-.6235 .9749,.2225 .4339,.901 -.4339,.901 -.9749,.2225 -.7818,-.6235"/>
          <polygon vector-effect="non-scaling-stroke" transform="scale(172.5)" points="0,-1 .7818,-.6235 .9749,.2225 .4339,.901 -.4339,.901 -.9749,.2225 -.7818,-.6235"/>
          <line x1="0" y1="0" x2="0" y2="-172.5"/>
          <line x1="0" y1="0" x2="134.9" y2="-107.6"/>
          <line x1="0" y1="0" x2="168.2" y2="38.4"/>
          <line x1="0" y1="0" x2="74.8" y2="155.4"/>
          <line x1="0" y1="0" x2="-74.8" y2="155.4"/>
          <line x1="0" y1="0" x2="-168.2" y2="38.4"/>
          <line x1="0" y1="0" x2="-134.9" y2="-107.6"/>
        </g>

        <g class="ticks" text-anchor="end">
          <text class="tick-label" x="-26" y="-167">0.5</text>
          <text class="tick-label" x="-26" y="-132">0.4</text>
          <text class="tick-label" x="-26" y="-98">0.3</text>
          <text class="tick-label" x="-26" y="-63">0.2</text>
          <text class="tick-label" x="-26" y="-29">0.1</text>
          <text class="tick-label" x="-26" y="6">0</text>
        </g>

        <g fill="none" stroke-width="4" stroke-linejoin="round">
          <polyline stroke="var(--charcoal)" points="-45.9,-36.6 0,-172.5 102.5,-81.7 168.2,38.4 25.5,52.9 -13.5,27.9"/>
          <polyline stroke="var(--orange)" points="22.5,46.7 -62.9,130.6 -168.2,38.4 -105.2,-83.9 0,-172.5 75.5,-60.2"/>
          <polyline stroke="var(--navy)" points="48.5,-38.7 168.2,38.4 74.8,155.4 -13.5,27.9"/>
          <polyline stroke="var(--sky)" points="-168.2,38.4 -75.5,-60.2"/>
        </g>
        <g>
          <circle cx="0" cy="0" r="6" fill="var(--grey)"/>
          <circle cx="-45.9" cy="-36.6" r="6" fill="var(--charcoal)"/>
          <circle cx="102.5" cy="-81.7" r="7" fill="var(--charcoal)"/>
          <circle cx="25.5" cy="52.9" r="6" fill="var(--charcoal)"/>
          <circle cx="-13.5" cy="27.9" r="6" fill="var(--charcoal)"/>
          <circle cx="168.2" cy="38.4" r="7" fill="var(--charcoal)"/>
          <circle cx="0" cy="-172.5" r="7" fill="var(--orange)"/>
          <circle cx="75.5" cy="-60.2" r="6" fill="var(--orange)"/>
          <circle cx="22.5" cy="46.7" r="6" fill="var(--orange)"/>
          <circle cx="-62.9" cy="130.6" r="6" fill="var(--orange)"/>
          <circle cx="-168.2" cy="38.4" r="7" fill="var(--orange)"/>
          <circle cx="-105.2" cy="-83.9" r="6" fill="var(--orange)"/>
          <circle cx="74.8" cy="155.4" r="7" fill="var(--navy)"/>
          <circle cx="-48.5" cy="-38.7" r="6" fill="var(--navy)"/>
          <circle cx="48.5" cy="-38.7" r="6" fill="var(--sky)"/>
          <circle cx="-75.5" cy="-60.2" r="6" fill="var(--sky)"/>
        </g>

        <g text-anchor="middle">
          <text class="axis-label" x="0" y="-190">n = 20</text>
          <text class="axis-label" x="188" y="-108">n = 100</text>
          <text class="axis-label" x="216" y="48">n = 30</text>
          <text class="axis-label" x="114" y="173">n = 70</text>
          <text class="axis-label" x="-114" y="173">n = 50</text>
          <text class="axis-label" x="-216" y="48">n = 30</text>
          <text class="axis-label" x="-190" y="-98">n = 50</text>
        </g>
      </g>
    </svg>

    <div class="analysis">
      <h2>Heading Here</h2>
      <p>Sed do eiusmod tempor incididunt ut labore et dolore magna aliqua. Ut enimad minim</p>
      <ul>
        <li>Duis aute irure dolor in reprehenderit in voluptate velit esse cillum</li>
        <li>dolore eu fugiat nulla pariatur. Excepteur sint occaecat cupidatat non</li>
        <li>proident, sunt inculpa qui officia deserunt mollit anim id est laborum.</li>
      </ul>
    </div>
    <p class="footnote">*Learners can select 1-2 rationales for each treatment ordered</p>
    <div class="bottom-bar">Clinova Education Confidential and Proprietary Information</div>
  </section>

</main>
</body>
</html>
```